Satchel & Compass needs new business card design

I need a new business card design. I'm looking for out-of-the-box design which represents the freedom of being a location independent entrepreneur.
I offer coaching, retreats and trips.
I would like to see designs with and without the photo.
Colors I use are black (#000000), green (#25A796) and brown (#D7C38C)
Website satchelandcompass.com

Target Market(s)

location independent entrepreneurs, digital nomads, people looking to swap the 9 to 5 for a lifestyle business

Industry/Entity Type

Business

Contact Information for Business Card

Petra Varga
Your Lifestyle Business Coach, Retreat & Trip Leader
http://satchelandcompass.com
hello@satchelandcompass.com
Live a life you don't need a holiday from

Font styles to use
Serif
Sans Serif

Requirements
Must have
• One side should contain only the logo. I would also consider having the "Live a life you don't need a holiday from" on that side too (depending on how it looks)
• Please show both sides on the designs.

```html
<!DOCTYPE html>
<html lang="en">
<head>
<meta charset="utf-8">
<title>Satchel &amp; Compass — Business Card</title>
<link rel="stylesheet" href="https://fonts.googleapis.com/css2?family=Questrial&display=swap">
<style>
  :root {
    --teal: #25A796;
    --teal-deep: #1f9a8a;
    --ink: #1a1a1a;
    --ink-soft: #3a3a3a;
    --paper: #fbfbfa;
    --stage: #e9e6e1;
    --rule: #2b2b2b;
  }
  * { box-sizing: border-box; margin: 0; padding: 0; }
  html, body {
    width: 1200px; height: 1023px; overflow: hidden;
    background: var(--stage);
    font-family: "Questrial", "Century Gothic", sans-serif;
  }
  .sheet {
    position: relative; width: 1200px; height: 1023px;
    display: flex; flex-direction: column; align-items: center; justify-content: center; gap: 64px;
  }
  .card {
    position: relative; width: 720px; height: 412px;
    box-shadow: 0 10px 28px rgba(0,0,0,.18);
  }
  /* front side */
  .card--front { background: var(--paper); color: var(--ink); }
  .brand {
    position: absolute; left: 56px; top: 58px;
    font-size: 40px; letter-spacing: .5px; color: var(--ink);
    display: flex; align-items: center; gap: 14px;
  }
  .brand__dot { width: 14px; height: 14px; border-radius: 50%; background: var(--teal); }
  .person { position: absolute; left: 56px; top: 176px; }
  .person__name { font-size: 25px; color: var(--teal); margin-bottom: 6px; }
  .person__role { font-size: 16.5px; line-height: 1.35; color: var(--ink-soft); }
  .divider {
    position: absolute; left: 330px; right: 48px; top: 222px;
    height: 1.5px; background: var(--rule);
  }
  .contacts {
    position: absolute; left: 56px; top: 282px; list-style: none;
    font-size: 16px; color: var(--ink-soft); line-height: 1.55;
  }
  .contacts li { display: flex; align-items: center; gap: 10px; }
  .contacts svg { width: 14px; height: 14px; flex: none; }
  .address {
    position: absolute; left: 470px; top: 250px;
    font-size: 16px; line-height: 1.4; color: var(--ink-soft);
  }
  /* back side */
  .card--back {
    background: linear-gradient(160deg, var(--teal) 0%, var(--teal-deep) 100%);
    color: #fff;
  }
  .back__brand {
    position: absolute; left: 0; right: 0; top: 150px; text-align: center;
    font-size: 62px; letter-spacing: 1px;
  }
  .back__tagline {
    position: absolute; left: 0; right: 0; bottom: 42px; text-align: center;
    font-size: 16px; letter-spacing: .3px; opacity: .92;
  }
</style>
</head>
<body>
<main class="sheet">
  <section class="card card--front" aria-label="Business card front">
    <div class="brand"><span class="brand__dot"></span>Satchel &amp; Compass</div>
    <div class="person">
      <p class="person__name">Petra Varga</p>
      <p class="person__role">Your Lifestyle Business Coach,<br>Retreat &amp; Trip Leader</p>
    </div>
    <div class="divider"></div>
    <ul class="contacts">
      <li>
        <svg viewBox="0 0 16 16" aria-hidden="true"><path fill="#25A796" d="M3.6 1.5l2.3 2.6-1.2 1.8c.9 2.1 2.6 3.8 4.6 4.7l1.8-1.2 2.6 2.3-1.3 2.3C7 13.9 2 9 1.3 2.8z"/></svg>
        +987 12 34 56 0
      </li>
      <li>
        <svg viewBox="0 0 16 16" aria-hidden="true"><rect x="1" y="3" width="14" height="10" fill="#25A796"/><path d="M1.5 3.5L8 9l6.5-5.5" stroke="#fff" stroke-width="1.3" fill="none"/></svg>
        hello@satchelandcompass.com
      </li>
      <li>
        <svg viewBox="0 0 16 16" aria-hidden="true"><circle cx="8" cy="8" r="6.5" fill="none" stroke="#25A796" stroke-width="1.5"/><ellipse cx="8" cy="8" rx="2.8" ry="6.5" fill="none" stroke="#25A796" stroke-width="1.2"/><path d="M1.5 8h13" stroke="#25A796" stroke-width="1.2"/></svg>
        www.satchelandcompass.com
      </li>
    </ul>
    <p class="address">Here your company or<br>home address</p>
  </section>

  <section class="card card--back" aria-label="Business card back">
    <p class="back__brand">Satchel &amp; Compass</p>
    <p class="back__tagline">Live a life you don't need a holiday from</p>
  </section>
</main>
</body>
</html>
```